Executive Summary

Create a one page executive summary of a venture fund - with the information here:
https://files.brindlepath.net/doc/7qR2mXvT9kLp4sWn8yZcB3fHj6dKa5eU/view?share=open

```html
<!DOCTYPE html>
<html lang="en">
<head>
<meta charset="utf-8">
<title>Halvard Decarbonization Partnership Fund – Executive Summary</title>
<link href="https://fonts.googleapis.com/css2?family=Figtree:ital,wght@0,400;0,500;0,600;0,700;0,800;1,800&family=Lora:wght@400;700&display=swap" rel="stylesheet">
<style>
:root{
  --navy:#1f3159;
  --navy-deep:#182848;
  --yellow:#f6bd3a;
  --yellow-soft:#f9c64a;
  --ink:#2a3550;
  --muted:#5a6275;
  --paper:#ffffff;
  --mist:#f2f2f2;
  --stage:#d4d4d4;
}
*{box-sizing:border-box;margin:0;padding:0}
html,body{width:1200px;height:1200px;overflow:hidden;background:var(--stage)}
body{font-family:"Figtree",sans-serif;color:var(--ink)}
.canvas{position:relative;width:1200px;height:1200px;background:var(--stage);overflow:hidden}
.page{position:absolute;top:298px;width:479px;height:672px;background:var(--paper);overflow:hidden}
.page--left{left:97px}
.page--right{left:620px}
.abs{position:absolute}

/* ---------- left page ---------- */
.brand{left:0;top:0;width:198px;height:86px;display:flex;align-items:center;justify-content:center;gap:6px}
.brand__mark{width:12px;height:12px;background:var(--navy)}
.brand__name{font-size:13px;font-weight:600;letter-spacing:2px;color:var(--navy)}
.hero{left:198px;top:0;width:281px;height:86px;background:linear-gradient(160deg,#5b6670 0%,#3b4a57 45%,#2c5a6a 80%,#3d7f8e 100%)}
.hero__kicker{position:absolute;left:22px;top:18px;font-family:"Lora",serif;font-size:13px;color:#fff}
.hero__title{position:absolute;left:22px;top:36px;font-family:"Lora",serif;font-weight:700;font-size:17px;line-height:19px;color:var(--yellow)}
.pitch{left:0;top:86px;width:201px;height:137px;background:var(--yellow)}
.pitch__text{position:absolute;left:26px;top:16px;font-size:12.4px;line-height:16.3px;color:var(--navy);border-left:2px solid var(--navy);padding-left:8px;width:170px}
.ecosystem{left:31px;top:167px;width:122px;height:122px;border-radius:50%;background:#fff;padding:8px}
.ecosystem__fill{width:100%;height:100%;border-radius:50%;background:radial-gradient(circle at 50% 50%,#1f3159 0%,#1f3159 30%,#e9ecf2 32%,#f4f1e6 100%)}
.thesis__bar{left:218px;top:98px;width:2px;height:35px;background:var(--navy)}
.thesis__title{left:228px;top:96px;font-size:12px;font-weight:700;color:var(--navy)}
.thesis__lede{left:228px;top:112px;font-size:7.2px;line-height:9.5px;color:var(--ink)}
.pillar{top:140px;width:70px}
.pillar__icon{width:27px;height:27px;display:block}
.pillar__name{margin-top:6px;font-size:6.8px;font-weight:700;color:var(--navy)}
.pillar__text{margin-top:2px;font-size:5px;line-height:6.6px;color:var(--muted)}
.divider{top:140px;height:72px;border-left:1px dashed #8a90a0}

.team{left:202px;top:223px;width:277px;height:282px;background:var(--navy)}
.member{position:absolute;width:134px}
.member__photo{position:absolute;width:34px;height:34px;border-radius:50%;border:1.5px solid var(--yellow);background:linear-gradient(150deg,#c8ccd4,#7c8494)}
.member__body{position:absolute;left:38px;top:-13px;width:100px}
.member__name{font-size:4.7px;line-height:5.8px;font-weight:700;color:#fff}
.member__role{font-size:4.7px;line-height:5.8px;font-weight:700;color:#fff}
.member__role em{font-style:normal;color:var(--yellow)}
.member__bio{margin-top:1px;font-size:4.5px;line-height:5.6px;color:#dfe3ec}

.focus__title{left:30px;top:302px;font-size:12px;font-weight:700;color:var(--navy)}
.focus__map{left:28px;top:325px;width:148px;height:57px;background:linear-gradient(180deg,#f1e1a6 0%,#d9dde6 40%,#c9ced8 100%)}
.focus__text{left:31px;top:394px;width:150px;font-size:7px;line-height:8.7px;color:var(--ink)}
.focus__list{left:31px;top:433px;width:150px;font-size:6px;line-height:7.8px;font-weight:700;color:var(--navy)}

.lower{left:0;top:483px;width:479px;height:189px;background:var(--mist)}
.lower__title{left:30px;top:504px;font-size:11.6px;line-height:15px;font-weight:700;color:var(--navy)}
.perk{position:absolute;background:#fff;border-radius:8px;overflow:hidden}
.perk__head{height:12px;background:var(--yellow);color:#fff;font-size:6px;font-weight:600;padding:2px 0 0 12px;border-radius:8px 8px 0 0}
.perk__row{display:flex;border-top:1px solid #e3e3e3}
.perk__key{background:var(--navy);color:#fff;font-weight:700;font-size:5.3px;line-height:6.5px;display:flex;align-items:center;padding:0 7px}
.perk__val{font-size:5.2px;line-height:6.5px;color:var(--muted);display:flex;align-items:center;padding:0 10px}

/* ---------- right page ---------- */
.terms__title{left:31px;top:25px;width:133px;height:17px;border:1.3px solid var(--navy);border-radius:6px;font-size:11px;font-weight:700;color:var(--navy);padding:1px 0 0 5px}
.term{position:absolute;left:31px;width:133px;display:flex;gap:2px}
.term__key{width:40px;background:var(--yellow);font-size:5px;font-weight:700;color:var(--navy);display:flex;align-items:center;padding-left:8px;line-height:6px}
.term__val{flex:1;background:#f1f1f1;font-size:5px;line-height:6.2px;color:var(--muted);display:flex;align-items:center;padding-left:6px}
.track__title{left:200px;top:62px;font-size:11.6px;font-weight:700;color:var(--navy)}
.track__note{left:203px;top:79px;width:80px;font-size:5.8px;line-height:7.3px;font-weight:700;color:var(--navy)}
.track__chart{left:289px;top:26px;width:152px;height:91px;background:#fbfaf7;border:1px solid #e6e6e6}
.rounds{left:191px;top:133px;width:268px;height:100px}
.rounds__row{display:flex;gap:1px;margin-bottom:1px}
.rounds__cell{background:var(--navy);color:#fff;font-size:4.6px;line-height:5.4px;height:16px;display:flex;align-items:center;padding-left:10px}
.rounds__row--head .rounds__cell{background:var(--yellow);color:var(--navy);font-weight:700;height:19px}
.c1{width:83px}.c2{width:88px}.c3{width:95px}
.rounds__row--head .c1{border-radius:8px 0 0 0}.rounds__row--head .c3{border-radius:0 8px 0 0}
.rounds__row:last-child .c1{border-radius:0 0 0 8px}.rounds__row:last-child .c3{border-radius:0 0 8px 0}

.portfolio__title{left:38px;top:250px;font-size:11.6px;font-weight:700;color:var(--navy)}
.shot{position:absolute}
.case__name{position:absolute;font-size:6.8px;line-height:8.4px;font-weight:700;color:var(--navy)}
.case__text{position:absolute;font-size:4.4px;line-height:5.6px;color:var(--muted)}
.quote{position:absolute;border:1px solid var(--navy);border-radius:10px;background:#fff}
.quote__mark{position:absolute;left:12px;top:-11px;font-family:"Lora",serif;font-size:24px;font-weight:700;color:var(--yellow);line-height:1;background:#fff;padding:0 2px}
.quote__text{position:absolute;left:12px;right:10px;top:8px;font-size:4.3px;line-height:5.6px;color:var(--ink)}
.quote__by{position:absolute;right:14px;font-size:4.3px;color:var(--ink);display:flex;align-items:center;gap:4px}
.quote__by::before{content:"";width:52px;border-top:0.7px solid var(--muted)}
.fund1__title{left:255px;top:511px;font-size:9.4px;line-height:12px;font-weight:700;color:var(--navy)}
.fund1__list{position:absolute;list-style:none;font-size:4.7px;line-height:5.6px;color:var(--ink)}
.fund1__list li{position:relative;padding-left:7px;margin-bottom:1.2px}
.fund1__list li::before{content:"";position:absolute;left:0;top:1.3px;width:3px;height:3px;border:0.7px solid var(--yellow);border-radius:50%}
.ask{left:251px;top:581px;width:201px;height:36px;background:#fff;border-radius:12px;box-shadow:0 1px 5px rgba(0,0,0,.14);font-size:10.6px;line-height:12.5px;font-weight:800;color:var(--navy);padding:5px 0 0 8px}
.footer{left:0;top:628px;width:479px;height:44px;display:flex}
.footer__cta{width:225px;background:var(--yellow);display:flex;align-items:center;padding-left:30px;gap:12px}
.footer__join{font-size:16px;font-weight:800;font-style:italic;color:var(--navy)}
.footer__hint{font-size:6.2px;font-weight:600;color:var(--navy);margin-top:4px}
.footer__contact{flex:1;background:var(--navy);display:flex;align-items:center;padding-left:18px;gap:9px;color:#fff;font-size:7px}
.footer__pill{background:var(--yellow);color:#fff;font-size:5.8px;font-weight:700;padding:1px 6px;border-radius:6px}
.footer__sep{height:11px;border-left:1px solid #fff}
.footer__mail{display:flex;align-items:center;gap:4px}
</style>
</head>
<body>
<div class="canvas">

  <!-- LEFT PAGE -->
  <section class="page page--left">
    <div class="abs brand"><span class="brand__mark"></span><span class="brand__name">HALVARD CAPITAL</span></div>
    <header class="abs hero" role="img" aria-label="Mountain lake landscape behind the title">
      <p class="hero__kicker">Executive Summary</p>
      <h1 class="hero__title">Halvard Decarbonization<br>Partnership Fund</h1>
    </header>

    <div class="abs pitch"><p class="pitch__text">Designed for Corporate Decarbonization Partnerships, Presented by Halvard Capital</p></div>

    <div class="abs ecosystem"><div class="ecosystem__fill" role="img" aria-label="Illustrated ecosystem diagram linking corporates, startups and the fund around climate tech investment innovation"></div></div>

    <div class="abs thesis__bar"></div>
    <h2 class="abs thesis__title">Thesis</h2>
    <p class="abs thesis__lede">Investing in Early Stage Decarbonization<br>Startup companies</p>

    <div class="abs pillar" style="left:223px">
      <svg class="pillar__icon" viewBox="0 0 27 27" aria-hidden="true"><circle cx="13.5" cy="13.5" r="13" fill="#f6bd3a"/><circle cx="13.5" cy="13.5" r="11" fill="#1f3159"/><path d="M8 15l3-3 3 2 5-4M8 17h11" stroke="#fff" stroke-width="1" fill="none"/></svg>
      <p class="pillar__name">Collaboration</p>
      <p class="pillar__text">Corporate LP network → collaborate on Deals, Insights, Co-investment, and Exits</p>
    </div>
    <div class="abs divider" style="left:303px"></div>
    <div class="abs pillar" style="left:317px">
      <svg class="pillar__icon" viewBox="0 0 27 27" aria-hidden="true"><circle cx="13.5" cy="13.5" r="13" fill="#f6bd3a"/><circle cx="13.5" cy="13.5" r="11" fill="#1f3159"/><path d="M9 18v-3M12 18v-5M15 18v-6M18 18v-8M8 19h11" stroke="#fff" stroke-width="1.1" fill="none"/></svg>
      <p class="pillar__name">Alpha</p>
      <p class="pillar__text">Next Generation of Solutions → Strategic &amp; financial returns</p>
    </div>
    <div class="abs divider" style="left:376px"></div>
    <div class="abs pillar" style="left:388px;width:80px">
      <svg class="pillar__icon" viewBox="0 0 27 27" aria-hidden="true"><circle cx="13.5" cy="13.5" r="13" fill="#f6bd3a"/><circle cx="13.5" cy="13.5" r="11" fill="#1f3159"/><rect x="8" y="9" width="11" height="9" rx="1" stroke="#fff" stroke-width="1" fill="none"/><path d="M10 15l2-2 2 1 3-3" stroke="#fff" stroke-width="0.9" fill="none"/></svg>
      <p class="pillar__name">Impact</p>
      <p class="pillar__text">≥2 Gt CO₂e reduction potential per portfolio reduced by 2050</p>
    </div>

    <div class="abs team">
      <!-- left column -->
      <div class="member" style="left:-16px;top:29px"><div class="member__photo" role="img" aria-label="Portrait of the managing partner" style="left:-1px;top:-17px"></div><div class="member__body"><p class="member__name">Lin (Mara) Hsu,</p><p class="member__role">Managing Partner <em>(California)</em></p><p class="member__bio">Climate Veteran over a decade. Policy maker, industry practitioner, founder and venture investor. M.S. from Ashford University</p></div></div>
      <div class="member" style="left:-16px;top:73px"><div class="member__photo" role="img" aria-label="Portrait of a venture partner" style="left:-1px;top:-17px"></div><div class="member__body" style="top:-24px"><p class="member__name">Pimchan Oravong,</p><p class="member__role">PhD, Venture Partner<em>(Thailand)</em></p><p class="member__bio">Faculty in Chemical Engineering at Chaophraya University. Industry expertise in bio-chemical engineering. PhD, B.S. in Chemical Engineering from Kingsley University, NIT</p></div></div>
      <div class="member" style="left:-16px;top:127px"><div class="member__photo" role="img" aria-label="Portrait of a venture partner" style="left:-1px;top:-17px"></div><div class="member__body" style="top:-27px"><p class="member__name">Kevin Tsao, PhD, Venture Partner</p><p class="member__role"><em>(New York)</em></p><p class="member__bio">Serial deep-tech entrepreneur. Industry expertise in photonics and semi-conductor. PhD in Applied Physics from Riverside University</p></div></div>
      <div class="member" style="left:-16px;top:170px"><div class="member__photo" role="img" aria-label="Portrait of the vice president" style="left:-1px;top:-17px"></div><div class="member__body" style="top:-21px"><p class="member__name">Dara Quan, CFA, Vice President <em style="font-style:normal;color:var(--yellow)">(California)</em></p><p class="member__bio">Veteran investor in energy transition. 10+ years of experience in capital markets, energy, sustainability and innovations. M.S. from Riverside University</p></div></div>
      <div class="member" style="left:-16px;top:210px"><div class="member__photo" role="img" aria-label="Portrait of the chief of staff" style="left:-1px;top:-17px"></div><div class="member__body" style="top:-10px"><p class="member__name">Elise Tan, Chief of Staff <em style="font-style:normal;color:var(--yellow)">(California)</em></p><p class="member__bio">Previous experience in M&amp;A and legal. M.S. from Riverside University</p></div></div>
      <div class="member" style="left:-16px;top:249px"><div class="member__photo" role="img" aria-label="Portrait of the legal advisor" style="left:-1px;top:-17px"></div><div class="member__body" style="top:-12px"><p class="member__name">Reid Hollis, J.D. Legal Advisor</p><p class="member__role"><em>(New York)</em></p><p class="member__bio">Senior Counsel at Corvex Technologies Capital, J.D. from Blue Ridge School of Law</p></div></div>
      <!-- right column -->
      <div class="member" style="left:128px;top:30px"><div class="member__photo" role="img" aria-label="Portrait of a venture partner" style="left:-1px;top:-17px"></div><div class="member__body" style="top:-18px;width:108px"><p class="member__name">Nira Sethakul, Ph.D.</p><p class="member__role">Venture Partner - <em>Artificial Intelligence</em></p><p class="member__bio">Nira received her B.S., M.S., and Ph.D. from Coral Bay University in Electrical Engineering.</p></div></div>
      <div class="member" style="left:128px;top:75px"><div class="member__photo" role="img" aria-label="Portrait of a venture partner" style="left:-1px;top:-17px"></div><div class="member__body" style="top:-22px;width:108px"><p class="member__name">Owen Calder Venture Partner</p><p class="member__role"><em>- Finance</em></p><p class="member__bio">Received his MBA in Entrepreneurship from the Harlow School and his BA in Psychology from Riverside University.</p></div></div>
      <div class="member" style="left:128px;top:128px"><div class="member__photo" role="img" aria-label="Portrait of a venture partner" style="left:-1px;top:-17px"></div><div class="member__body" style="top:-23px;width:108px"><p class="member__name">Owen Calder Venture Partner</p><p class="member__role"><em>- Finance</em></p><p class="member__bio">Ivy received her MBA from the Harlow School and her B.A. in Economics and Finance from Qinghe University.</p></div></div>
      <div class="member" style="left:128px;top:182px"><div class="member__photo" role="img" aria-label="Portrait of an advisor" style="left:-1px;top:-17px"></div><div class="member__body" style="top:-21px;width:108px"><p class="member__name">Martin (Marty) Vale,</p><p class="member__role"><em>Ph.D Advisor</em></p><p class="member__bio">Dr. Vale holds a Ph.D. from Northfield School of Management and a B.S. from Larkmoor University.</p></div></div>
      <div class="member" style="left:128px;top:236px"><div class="member__photo" role="img" aria-label="Portrait of an advisor" style="left:-1px;top:-17px"></div><div class="member__body" style="top:-26px;width:108px"><p class="member__name">Adrian Lowe Advisor -</p><p class="member__role"><em>Director of Sustainability Initiative, Northfield School of Management</em></p><p class="member__bio">Dr. Lowe holds a Ph.D. in Organization Studies from Northfield, a Master's in Education and AB in Psychology from Whitcombe University.</p></div></div>
    </div>

    <h2 class="abs focus__title">Investment Focus</h2>
    <div class="abs focus__map" role="img" aria-label="Matrix of decarbonization sub-sectors by investment focus"></div>
    <p class="abs focus__text">We Invest in Frontier Decarbonization Technologies that Generate Venture Returns and Strategic Values for corporate LPs, such as:</p>
    <p class="abs focus__list">AI &amp; Robotics in Energy Efficiency | Data Centers Decarbonization | Clean Energy Infrastructure Synthetic Biology &amp; Advanced Material | Sustainable Fuel | Electrification Enabler | Adaptation</p>

    <div class="abs lower"></div>
    <h2 class="abs lower__title">Maximize strategic and<br>financial return</h2>

    <div class="perk" style="left:29px;top:542px;width:159px;height:53px">
      <div class="perk__head">Deal Flow Access</div>
      <div class="perk__row" style="height:20px"><div class="perk__key" style="width:49px">Weekly Deal Reviews</div><div class="perk__val">Join sessions to evaluate up to 8 startups/week</div></div>
      <div class="perk__row" style="height:21px"><div class="perk__key" style="width:49px">Startup Pipeline</div><div class="perk__val">Access 500+ curated startup opportunities/year</div></div>
    </div>
    <div class="perk" style="left:29px;top:602px;width:159px;height:53px">
      <div class="perk__head">Informed Co-Investment</div>
      <div class="perk__row" style="height:20px"><div class="perk__key" style="width:58px">Co-Investment Network</div><div class="perk__val">Partner with other corporates to support portfolio</div></div>
      <div class="perk__row" style="height:21px"><div class="perk__key" style="width:58px">Due Diligence Digest</div><div class="perk__val">Receive structured co-investment insights and summaries</div></div>
    </div>
    <div class="perk" style="left:208px;top:514px;width:246px;height:66px">
      <div class="perk__head">Sector Intelligence</div>
      <div class="perk__row" style="height:18px"><div class="perk__key" style="width:72px">Research Theses</div><div class="perk__val">Access 10+ original sector insights per year</div></div>
      <div class="perk__row" style="height:18px"><div class="perk__key" style="width:72px">Knowledge Exchange</div><div class="perk__val">Collaborate on emerging trends and sub-sector opportunities</div></div>
      <div class="perk__row" style="height:18px"><div class="perk__key" style="width:72px">Sector Workshops</div><div class="perk__val">Attend online workshops focused on thematic deep-dives</div></div>
    </div>
    <div class="perk" style="left:208px;top:588px;width:246px;height:67px">
      <div class="perk__head">Tailored Engagement (Dependent on Investment Level)</div>
      <div class="perk__row" style="height:18px"><div class="perk__key" style="width:72px">Custom Deal Sourcing</div><div class="perk__val">Focused pipeline by sub-sector interest</div></div>
      <div class="perk__row" style="height:18px"><div class="perk__key" style="width:72px">Private Sector Briefings</div><div class="perk__val">Bespoke analysis tailored to LP strategic needs</div></div>
      <div class="perk__row" style="height:18px"><div class="perk__key" style="width:72px">Strategic GP Access</div><div class="perk__val">Collaborate via co-investments or advisory roles based on</div></div>
    </div>
  </section>

  <!-- RIGHT PAGE -->
  <section class="page page--right">
    <h2 class="abs terms__title">Fund Term Overview</h2>
    <div class="term" style="top:48px;height:14px"><span class="term__key">Fund Size</span><span class="term__val">$100M</span></div>
    <div class="term" style="top:66px;height:14px"><span class="term__key">Term</span><span class="term__val">10+1+1 Years</span></div>
    <div class="term" style="top:84px;height:21px"><span class="term__key">Stage</span><span class="term__val">Pre-seed - Series B (Seed / Series A focus)</span></div>
    <div class="term" style="top:108px;height:21px"><span class="term__key">Target Returns</span><span class="term__val">3x of Invested Capital / 15%-25% IRR</span></div>
    <div class="term" style="top:132px;height:14px"><span class="term__key" style="width:59px">Portfolio Number</span><span class="term__val">30</span></div>
    <div class="term" style="top:150px;height:14px"><span class="term__key">Check Size</span><span class="term__val" style="padding-left:2px">$0.25M - $5M (stage-dependent)</span></div>
    <div class="term" style="top:168px;height:14px"><span class="term__key" style="width:59px">Follow-on Reserve</span><span class="term__val">50%</span></div>
    <div class="term" style="top:186px;height:28px"><span class="term__key">Fee</span><span class="term__val">2.5% during investment period. Step down: 10% annually after the investment period. Floor: 1.5%</span></div>
    <div class="term" style="top:218px;height:14px"><span class="term__key">Carry</span><span class="term__val">20%</span></div>

    <h2 class="abs track__title">Track Record</h2>
    <p class="abs track__note">Over 4.11x MOIC for SPV deals (unweighted and unrealized)</p>
    <svg class="abs track__chart" viewBox="0 0 152 91" aria-label="Bar chart of current and projected MOIC by company">
      <text x="6" y="9" font-family="Figtree,sans-serif" font-size="4.5" fill="#333">Multiple (x)</text>
      <rect x="52" y="6" width="3" height="3" fill="#f6bd3a"/><text x="57" y="8.7" font-family="Figtree,sans-serif" font-size="3" fill="#333">Current MOIC</text>
      <rect x="84" y="6" width="3" height="3" fill="#1f5fbf"/><text x="89" y="8.7" font-family="Figtree,sans-serif" font-size="3" fill="#333">Projected next round MOIC</text>
      <g stroke="#e2e2e2" stroke-width="0.4"><line x1="14" y1="20" x2="148" y2="20"/><line x1="14" y1="33" x2="148" y2="33"/><line x1="14" y1="46" x2="148" y2="46"/><line x1="14" y1="59" x2="148" y2="59"/><line x1="14" y1="72" x2="148" y2="72"/></g>
      <g fill="#f6bd3a">
        <rect x="18" y="26" width="3" height="46"/><rect x="31" y="39" width="3" height="33"/><rect x="44" y="61" width="3" height="11"/><rect x="57" y="65" width="3" height="7"/><rect x="70" y="69" width="3" height="3"/><rect x="83" y="69" width="3" height="3"/><rect x="96" y="69" width="3" height="3"/><rect x="109" y="68" width="3" height="4"/><rect x="122" y="68" width="3" height="4"/><rect x="135" y="69" width="3" height="3"/>
      </g>
      <g fill="#1f5fbf">
        <rect x="35" y="50" width="3" height="22"/><rect x="48" y="65" width="3" height="7"/><rect x="74" y="61" width="3" height="11"/><rect x="87" y="66" width="3" height="6"/><rect x="100" y="65" width="3" height="7"/><rect x="113" y="65" width="3" height="7"/><rect x="126" y="67" width="3" height="5"/>
      </g>
      <g font-family="Figtree,sans-serif" font-size="3" fill="#444">
        <text transform="translate(15 84) rotate(-45)">Labwell</text><text transform="translate(28 86) rotate(-45)">GridLoom</text><text transform="translate(41 84) rotate(-45)">Lumen</text><text transform="translate(54 84) rotate(-45)">FigTree</text><text transform="translate(67 84) rotate(-45)">Tintora</text><text transform="translate(80 84) rotate(-45)">Lumaxa</text><text transform="translate(93 84) rotate(-45)">Proteanic</text><text transform="translate(106 84) rotate(-45)">Fibrevia</text><text transform="translate(119 84) rotate(-45)">Methavolt</text><text transform="translate(132 84) rotate(-45)">VoltRoam</text>
      </g>
    </svg>

    <div class="abs rounds">
      <div class="rounds__row rounds__row--head"><span class="rounds__cell c1">Company Finished Next Priced Round</span><span class="rounds__cell c2">Stage Invested</span><span class="rounds__cell c3">Current stage</span></div>
      <div class="rounds__row"><span class="rounds__cell c1">Labwell</span><span class="rounds__cell c2">Series A Bridge 2020</span><span class="rounds__cell c3">Series C $1.8B</span></div>
      <div class="rounds__row"><span class="rounds__cell c1">GridLoom</span><span class="rounds__cell c2">Seed 2019</span><span class="rounds__cell c3">Growth Stage $220M (Need updated data)</span></div>
      <div class="rounds__row"><span class="rounds__cell c1">Lumen Stones</span><span class="rounds__cell c2">Seed 2021</span><span class="rounds__cell c3">Series A $73M</span></div>
      <div class="rounds__row"><span class="rounds__cell c1">Fig Tree Infrastructure</span><span class="rounds__cell c2">Seed Extension 2021</span><span class="rounds__cell c3"></span></div>
      <div class="rounds__row"><span class="rounds__cell c1">Tintora.Bio</span><span class="rounds__cell c2">Pre-Seed 2019</span><span class="rounds__cell c3">Series A $35M</span></div>
    </div>

    <h2 class="abs portfolio__title">Example Portfolio Startups</h2>

    <div class="shot" role="img" aria-label="Modular methanol production unit" style="left:29px;top:270px;width:124px;height:50px;background:linear-gradient(180deg,#e8e8e8,#9a9ea3)"></div>
    <p class="case__name" style="left:29px;top:328px">Methavolt: modular green methanol production</p>
    <p class="case__text" style="left:29px;top:342px;width:190px">The spin out company has developed a proprietary process to synthesize commodity chemicals, starting with green methanol and ammonia, at cost-parity using used diesel engines. By converting these engines to consume inputs such as methane, biogas, and carbon dioxide, the company has created a low-carbon process to produce these chemicals by displacing the need for flaring or release of methane, plugging into waste streams offsite.</p>
    <div class="quote" style="left:26px;top:390px;width:185px;height:43px"><span class="quote__mark">“</span><p class="quote__text">It has been a pleasure working with Halvard Capital and having them on our cap table. Their team is well connected, always available and eager to help"</p><p class="quote__by" style="top:30px">Nikolas Varga, Co-founder &amp; CEO at</p></div>

    <div class="shot" role="img" aria-label="Two founders standing beside algae bioreactor tubes" style="left:30px;top:444px;width:170px;height:53px;background:linear-gradient(180deg,#b9c6cf 0%,#7d8f86 50%,#3d5a3c 100%)"></div>
    <p class="case__name" style="left:30px;top:503px">Proteanic: real meat protein alternatively<br>made at price parity</p>
    <p class="case__text" style="left:30px;top:521px;width:186px">Inserted animal genes into microalgae and grow recombinant protein with sun and air. Developing recombinant animal matrix proteins made from carbon dioxide to make alternative meat and seafood. Recombinant proteins are those that are manipulated so they can produce in larger quantities.</p>
    <div class="quote" style="left:26px;top:559px;width:185px;height:51px"><span class="quote__mark">“</span><p class="quote__text">Halvard Capital has provided invaluable support through its broad network in the USA and Southeast Asia. Having boots on the ground has helped us gain credibility with corporations and business partners in these markets. The personal connections of Pimchan and Mara have opened doors for us and played a crucial role in pushing forward key deals.</p><p class="quote__by" style="top:41px">Yoav Arad, CEO and Co-founder, Proteanic</p></div>

    <div class="shot" role="img" aria-label="Recycled carbon fiber strands with a recycling symbol" style="left:248px;top:260px;width:169px;height:54px;background:linear-gradient(135deg,#2b2e33 0%,#55595f 45%,#c26a2a 60%,#3a3d42 100%)"></div>
    <p class="case__name" style="left:248px;top:325px">Fibrevia: recycled scraped carbon fiber<br>into virgin grade carbon fiber</p>
    <p class="case__text" style="left:248px;top:345px;width:206px">Fibrevia is an advanced materials startup focused on recycling carbon fiber-reinforced composites, enabling lightweight, high-performance materials to be reused across automotive, sporting goods, and industrial sectors. Its patented low-cost, energy-efficient process recovers high-quality carbon fiber from manufacturing scrap and end-of-life products, providing a sustainable alternative to virgin carbon fiber. With growing demand for lightweight, sustainable materials, Fibrevia plays a key role in advancing circular economy solutions for high-performance composites.</p>
    <div class="quote" style="left:245px;top:403px;width:214px;height:102px"><span class="quote__mark">“</span><p class="quote__text">Halvard Capital has been a supportive partner since our very first meeting. They took a disciplined data driven approach to their investment decision making process and they continue to use these skills to help guide their founders through the peaks and valleys of the portfolio lifecycle. Lin understands the opportunities and challenges facing sustainability focused entrepreneurs as she is an innovator herself. She is bringing insightful perspectives and fresh ideas to climate capital. Halvard investment model is more than just capital though. The team has a vast global network which Fibrevia has been able to leverage for introductions to potential customers and partners. This was evidenced through Climasphere 2024 and the critical connections I made there. I'm excited to be associated with the world class investments in Halvard Capital Fund I and I'm grateful for the support Fibrevia continues to receive as a portfolio company</p><p class="quote__by" style="top:90px">Brent Holloway, Co-Founder &amp; CEO, Fibrevia</p></div>

    <h2 class="abs fund1__title">Fund I Investments so far<br>(continue to invest)</h2>
    <ul class="fund1__list" style="left:256px;top:543px;width:95px">
      <li>Lumaxa, former Triad Nano (Seed, raising Series A)</li>
      <li>Methavolt (Seed, raising Series A)</li>
      <li>Fibrevia (Series A, will raise Series B)</li>
    </ul>
    <ul class="fund1__list" style="left:355px;top:543px;width:100px">
      <li>Proteanic (Seed)</li>
      <li>Methavolt Via Biofuels (Pre-seed)</li>
      <li>VoltRoam (Seed)</li>
    </ul>

    <p class="abs ask">SERIES B 95M POST MONEY FOR<br>CURRENT STAGE FOR FIG TREE?</p>

    <footer class="abs footer">
      <div class="footer__cta"><span class="footer__join">Join Us</span><span class="footer__hint">For any inquiries, please contact</span></div>
      <div class="footer__contact">
        <span class="footer__pill">Mara Hsu</span>
        <span>Managing Partner</span>
        <span class="footer__sep"></span>
        <span class="footer__mail"><svg width="10" height="7" viewBox="0 0 10 7" aria-hidden="true"><rect x="0.5" y="0.5" width="9" height="6" fill="none" stroke="#fff" stroke-width="0.8"/><path d="M0.5 0.5L5 4l4.5-3.5" fill="none" stroke="#fff" stroke-width="0.8"/></svg>mhsu@halvardcapital.example</span>
      </div>
    </footer>
  </section>

</div>
</body>
</html>
```